price list for web and print- sending to inquiring clients and use as promo material

Hello
I need a graphic design for my photography price list/s. I am a people photographer. The first of 6 price sheets will be for head shots- I would like a price sheet that captures the prospective clients' attention. The info and visual should be compelling and easy to digest. It should be simple yet interesting. I will provide you with some pictures but you do not have to include them. I have a studio indoors and outdoors also working on location. This design should be for email and print. The picture of "ingrid" is me and I use that on all my profiles. I like the fonts in the logo but it is too boxy and rigid

Target Market(s)

repeat client, word of mouth referrals, new people but aquaintances of others that might know me

Industry/Entity Type

Graphic Design

Font styles to use
Serif
Sans Serif
Script

Requirements
Must have
• prices and maybe some words about my services that I sent in... Please tie it together as best as possible..
Nice to have
• Loosen up my logo.. it is in a box.....contemporary design but not something that would not fit in with corporate.. I like this headline
• "Create a great first impression with your professional headshots"
• I sent in other copy and my logo(sent in the picture drop box)

```html
<!DOCTYPE html>
<html lang="en">
<head>
<meta charset="utf-8">
<title>Ingrid M. Hale Photography – Headshot Price List</title>
<link rel="stylesheet" href="https://fonts.googleapis.com/css2?family=Open+Sans:wght@400;600&family=Special+Elite&display=swap">
<style>
  :root {
    --panel-grey: #575757;
    --panel-grey-light: #6a6a6a;
    --section-grey: #3e3e3e;
    --footer-black: #111111;
    --box-black: #141414;
    --ink-white: #ffffff;
    --ink-soft: #c9c9c9;
    --ink-muted: #a9a9a9;
    --ink-faded: #5e5e5e;
    --accent-pink: #ec1163;
    --accent-yellow: #fcc11c;
    --photo-light: #a9b0b6;
    --photo-dark: #5b6168;
  }
  * { box-sizing: border-box; margin: 0; padding: 0; }
  html, body { width: 800px; height: 1200px; overflow: hidden; background: #ffffff; }
  .sheet {
    position: relative; width: 800px; height: 1200px; overflow: hidden;
    background: linear-gradient(180deg, var(--panel-grey) 0%, var(--panel-grey-light) 45%, var(--panel-grey) 100%);
    font-family: "Open Sans", Arial, sans-serif;
  }

  /* Brand name */
  .brand {
    position: absolute; left: 0; top: 0; width: 193px; height: 83px;
    background: #000; display: flex; align-items: center; justify-content: center;
    color: var(--ink-white); font-family: "Open Sans", Arial, sans-serif;
    font-weight: 600; font-size: 17px; line-height: 22px; text-align: center;
  }
  .brand-rule { position: absolute; left: 0; top: 83px; width: 193px; height: 6px; background: var(--accent-pink); }
  .brand-edge { position: absolute; left: 193px; top: 0; width: 4px; height: 89px; background: var(--accent-yellow); }

  /* Portrait area */
  .portrait { position: absolute; left: 340px; top: 0; width: 460px; height: 727px; }
  .portrait-photo {
    position: absolute; inset: 0;
    background: radial-gradient(ellipse at 60% 35%, var(--photo-light) 0%, var(--photo-dark) 80%);
  }
  .portrait-shapes { position: absolute; inset: 0; }

  /* Packages */
  .package {
    position: absolute; z-index: 2; background: var(--box-black); color: var(--ink-soft);
    font-family: "Special Elite", "Courier New", monospace; font-variant: small-caps;
  }
  .package-title {
    font-family: "Open Sans", Arial, sans-serif; font-variant: normal; letter-spacing: 0;
    font-weight: 400; color: var(--ink-white); text-transform: uppercase;
  }
  .package .price { color: var(--accent-pink); }
  .package .indent { padding-left: 18px; }

  .package-entry { left: 13px; top: 151px; width: 313px; height: 167px; padding: 1px 14px 0;
    font-size: 16px; line-height: 24px; letter-spacing: 2.6px; }
  .package-entry .package-title { font-size: 16px; line-height: 20px; margin-bottom: 1px; }
  .package-entry .price { padding-left: 18px; }

  .package-two { left: 13px; top: 331px; width: 313px; height: 169px; padding: 0 4px;
    font-size: 13.5px; line-height: 21.4px; letter-spacing: 1.5px; }
  .package-two .package-title { font-size: 14px; line-height: 19px; margin-top: 1px; }

  .package-premier { left: 0; top: 507px; width: 340px; height: 237px; padding: 0 6px;
    font-size: 14.5px; line-height: 23px; letter-spacing: 1.5px; }
  .package-premier .package-title { font-family: "Special Elite", "Courier New", monospace; font-variant: small-caps;
    text-transform: none; letter-spacing: 1.6px; color: var(--ink-muted); font-size: 16px; line-height: 26px; }
  .package-premier .faded { color: var(--ink-faded); }

  /* Studio intro */
  .studio { position: absolute; z-index: 1; left: 0; top: 727px; width: 800px; height: 308px; background: var(--section-grey); }
  .studio-rule { position: absolute; left: 27px; top: 46px; width: 4px; height: 213px; background: var(--accent-pink); }
  .studio-heading { position: absolute; left: 47px; top: 40px; color: var(--ink-white); font-size: 27px; line-height: 36px; font-weight: 400; }
  .studio-heading .accent { color: var(--accent-pink); }
  .studio-text { position: absolute; left: 47px; top: 114px; width: 335px; color: var(--ink-muted);
    font-size: 17.5px; line-height: 24.5px; hyphens: auto; -webkit-hyphens: auto; }

  /* Contact footer */
  .contact { position: absolute; left: 0; top: 1035px; width: 800px; height: 165px; background: var(--footer-black); text-align: center; }
  .contact-address { position: absolute; left: 0; right: 0; top: 60px; color: var(--ink-white); font-size: 17px; font-weight: 600; }
  .contact-online { position: absolute; left: 0; right: 0; top: 95px; color: var(--accent-pink); font-size: 17px; font-weight: 600; }
  .contact .dot { margin: 0 8px; }
  .contact-rule { position: absolute; left: 143px; top: 133px; width: 524px; height: 5px; background: var(--accent-pink); }
</style>
</head>
<body>
<main class="sheet">
  <div class="brand">Ingrid M. Hale<br>Photography</div>
  <div class="brand-rule"></div>
  <div class="brand-edge"></div>

  <section class="portrait">
    <div class="portrait-photo" role="img" aria-label="Studio headshot portrait of a smiling businessman in a dark suit with arms crossed"></div>
    <svg class="portrait-shapes" width="460" height="727" viewBox="0 0 460 727" aria-hidden="true">
      <polygon points="0,0 393,0 0,193" fill="var(--accent-yellow)"/>
      <polygon points="0,687 460,424 460,727 0,727" fill="var(--accent-pink)"/>
    </svg>
  </section>

  <section class="package package-entry">
    <h2 class="package-title">Entry Package</h2>
    <p>Quick and Simple</p>
    <p class="indent">one pose</p>
    <p class="indent">one wardrobe</p>
    <p class="indent">one selected image re-touched</p>
    <p class="price">just $175</p>
  </section>

  <section class="package package-two">
    <h2 class="package-title">2 Pose Package</h2>
    <p>Most Popular</p>
    <p>&nbsp;two poses</p>
    <p>&nbsp;Two wardrobe changes</p>
    <p>&nbsp;Two selected images retouched</p>
    <p>&nbsp;One or two background changes</p>
    <p>&nbsp;just $175</p>
    <p>&nbsp;Additional images just <span class="price">$75 each</span></p>
  </section>

  <section class="package package-premier">
    <h2 class="package-title">Premier Package</h2>
    <p>Get it all</p>
    <p>Most Popular</p>
    <p>four poses|3-4 wardrobe changes</p>
    <p>4 selected images retouched</p>
    <p>2-3 background changes</p>
    <p>Additional images just $75 each</p>
    <p>optional outdoor studio</p>
    <p>Just $525</p>
    <p class="faded">Additional images just <span class="price">$75 each</span></p>
  </section>

  <section class="studio">
    <div class="studio-rule"></div>
    <h1 class="studio-heading">PROFESSIONAL<br>PHOTOGRAPHY <span class="accent">STUDIO</span></h1>
    <p class="studio-text">Ingrid Is an Accomplished Photographer Who Have helped thousand of Clients. She is an Expert at Helping Client Confident and Approachable. And can Complete a Photo-Shoot In 30 Minutes or More.</p>
  </section>

  <footer class="contact">
    <p class="contact-address">1840 Linden Crest Parkway<span class="dot">•</span>Maplewood GA 30399<span class="dot">•</span>404-555-0148</p>
    <p class="contact-online">imhphoto@lumenmail.com<span class="dot">•</span>http://imhphoto.com</p>
    <div class="contact-rule"></div>
  </footer>
</main>
</body>
</html>
```